Firm of surveyors needs a professional yet friendly looking flyer

Our company offers help to landlords who have a phone mast on their property. We help them to negotiate the best rent and lease terms. There are so many landlords who don't seek professional advice because they don't know it's available. We want to send them a flyer which is informative, looks professional but also friendly so it prompts them to call us. I have attached the wording and some pictures but have more I can send but they were too large to attach.

Target Market(s)

Ranges from farmers to large corporations and land owners

Industry/Entity Type

Surveyor

Font styles to use
Sans Serif

Colors
acd136
9bcb3c
000000
ffffff
606060
848484

Requirements
Must have
• Must be clear, must give a professional look, must include pictures, must include our logo, must use our colour scheme (or variations of it). Ideally, I would like a try-fold design if possible.
Nice to have
• I would like there to be stand out lines to catch the readers eye (I have included some on the wording document). I would like a clean and modern design
Should not have
• Should not be too fussy

```html
<!DOCTYPE html>
<html lang="en">
<head>
<meta charset="utf-8">
<title>Phone Mast Advice – Tri-fold Flyer</title>
<link rel="stylesheet" href="https://fonts.googleapis.com/css2?family=Open+Sans:wght@400;600&family=Roboto:wght@500;700&display=swap">
<style>
  :root {
    --page-bg: #e9e9e6;
    --paper: #ffffff;
    --ink: #1f1f1f;
    --green-deep: #2f5a2a;
    --green-mid: #4a7a3a;
    --green-light: #6f9a55;
    --green-bullet: #3f6b33;
    --sky-blue: #3e74c2;
    --white: #ffffff;
  }
  * { box-sizing: border-box; margin: 0; padding: 0; }
  html, body { width: 1200px; height: 906px; overflow: hidden; }
  body { background: var(--page-bg); position: relative; font-family: "Open Sans", Arial, sans-serif; }

  .flyer {
    position: absolute; left: 77px; top: 64px; width: 1044px; height: 739px;
    background: var(--paper); box-shadow: 0 2px 6px rgba(0,0,0,.25);
    overflow: hidden;
  }
  .panel { position: absolute; top: 0; height: 739px; }
  .panel--intro { left: 0; width: 341px; background: var(--paper); }
  .panel--info { left: 341px; width: 703px; }
  .field-backdrop {
    position: absolute; inset: 0;
    background: linear-gradient(180deg, #2e5b2c 0%, #46703a 40%, #5e8452 62%, #3e6834 80%, #2f4f28 100%);
  }
  .services {
    position: absolute; left: 363px; top: 340px; width: 340px; height: 399px;
    background: var(--paper);
  }

  .body-copy { font-size: 12px; line-height: 16px; color: var(--ink); }
  .body-copy p + p { margin-top: 16px; }
  .body-copy--light { color: var(--white); }

  .intro-copy { position: absolute; left: 36px; top: 34px; width: 262px; }
  .mast-photo {
    position: absolute; left: 23px; top: 557px; width: 287px; height: 149px;
    background: linear-gradient(180deg, #2f66b8, var(--sky-blue) 60%, #5a8ad0);
  }

  .section { position: absolute; left: 35px; width: 296px; }
  .section__title {
    background: var(--white); color: var(--green-mid);
    font-family: "Roboto", Arial, sans-serif; font-weight: 700; font-size: 18px;
    text-align: center; height: 33px; line-height: 33px;
  }
  .section__text { margin: 21px 18px 0 10px; }
  .section--sell { top: 28px; }
  .section--get { top: 281px; }
  .section--climate { top: 514px; }

  .climate-copy { position: absolute; left: 402px; top: 34px; width: 274px; }
  .callout {
    position: absolute; left: 400px; top: 290px; width: 278px;
    font-family: "Roboto", Arial, sans-serif; font-weight: 700; font-size: 14px;
    line-height: 18px; color: var(--white); text-align: center;
  }

  .services__title {
    position: absolute; left: 34px; top: 23px; width: 290px; height: 33px;
    background: var(--green-mid); color: var(--white);
    font-family: "Roboto", Arial, sans-serif; font-weight: 500; font-size: 18px;
    text-align: center; line-height: 33px;
  }
  .services__list {
    position: absolute; left: 26px; top: 75px; list-style: none;
    font-family: "Roboto", Arial, sans-serif; font-weight: 500; font-size: 17.5px;
    color: var(--green-mid);
  }
  .services__list li { height: 26.2px; line-height: 26px; padding-left: 27px; position: relative; white-space: nowrap; }
  .services__list li::before {
    content: ""; position: absolute; left: 0; top: 7px; width: 13px; height: 13px;
    border-radius: 50%; background: var(--green-bullet);
  }
</style>
</head>
<body>
  <main class="flyer">
    <section class="panel panel--intro">
      <div class="intro-copy body-copy">
        <p>Many of the original mobile phone mast leases / agreements are now coming up for renewal. This is an ideal opportunity for landlords to achieve the best deal. We are currently offering to review telecoms leases for free and provide landlords with our recommendations. If you would like to take us up on this free no obligation offer, send a copy of your agreement and any recent correspondence to us, either via post or email using the details on this flyer. Please also provide us with your name, contact number and let us know the current rent you are achieving so we can see if there is room for improvement. Once we have received this, one of our surveyors will give you a call when convenient to talk through your lease with you, highlighting anything we feel needs addressing, any opportunity to increase the rent, or to discuss a specific issue you are having with your mast (i.e. an upgrade request).</p>
        <p>Recently, operators have been attempting to cut costs by reducing rents. They are joining forces in an effort to drive rents down. Many landlords are contacting us after receiving a letter from the operators / operator’s agent, telling them they must accept a rent reduction or risk losing their site. In the majority of cases, The Mast Advice Group can prevent this from occurring and protect the landlord’s rental income.</p>
      </div>
      <div class="mast-photo" role="img" aria-label="Photograph of a mobile phone mast with antennas against a blue sky"></div>
    </section>

    <section class="panel panel--info">
      <div class="field-backdrop" role="img" aria-label="Soft green photograph of a grassy field"></div>

      <article class="section section--sell">
        <h2 class="section__title">Sell your phone mast</h2>
        <p class="section__text body-copy body-copy--light">We can also assist landlords in selling their phone mast. We have strong links with many large investors who regularly purchase the freehold or leasehold interest of masts and will pay a cash lump sum of tens, even hundreds of thousands of pounds. This can be done in a matter of weeks and the cash is yours to spend however you like, regardless of whether the mast stays for the duration of the investors leasehold or not. We can negotiate flexible terms, such as a buyback option so please call us today to discuss.</p>
      </article>

      <article class="section section--get">
        <h2 class="section__title">Getting a phone mast</h2>
        <p class="section__text body-copy body-copy--light">If you don’t currently have a mast located on your land but are interested in receiving thousands of pounds a year in rental income, or you have a redundant mast you would like to market, we offer a free advertising service on our website. We will market your land to phone mast operators with a view to having a mast located there. Please visit the ‘Advertise My Site’ link on our website to take advantage of this service.</p>
      </article>

      <article class="section section--climate">
        <h2 class="section__title">The current telecoms climate</h2>
        <p class="section__text body-copy body-copy--light">The telecoms market, in relation to mobile phone masts, is going through some huge changes. Operators are combining to cut costs. We have already seen Tricell join forces with Telvane and Oxon Mobile form a jointly owned company with Vantel called SiteShare Ltd. More recently, Telvane and Amberline have merged to form Allwave Networks Ltd to become the new network leader.</p>
      </article>

      <div class="climate-copy body-copy body-copy--light">
        <p>What this can mean for the landlord is changes to their site and potentially the loss of income. It can all be very confusing but don’t worry, this is where we can help. We know the telecoms industry and understand how a new situation may affect a landlord, therefore, allowing us to provide the best advice on protecting your asset.</p>
        <p>In April 2017, the Government introduced the Digital Economy Act. This sets out significant changes for landlords, including the way rents are calculated. We have already seen operators contact landlords, trying to reduce their rent in light of this new law. We are working alongside specialist telecoms solicitors to try to reduce the potential negative impact on landlords.</p>
      </div>
      <p class="callout">Landlords should not sign anything until they have sought professional advice</p>

      <aside class="services">
        <h2 class="services__title">Our Services</h2>
        <ul class="services__list">
          <li>Rent Reviews</li>
          <li>Lease Renewals</li>
          <li>Network Consolidation Issues</li>
          <li>Site Shares</li>
          <li>Rent Protection</li>
          <li>Equipment Upgrades</li>
          <li>Mast Removals / Decommissioning</li>
          <li>Mast Sales and Marketing</li>
          <li>Land Marketing for Masts</li>
          <li>Mast Management and Portfolios</li>
          <li>Safety Testing</li>
        </ul>
      </aside>
    </section>
  </main>
</body>
</html>
```